Website design for a Fine Food exhibition in Asia

We need a website design for a Food and Wine exhibition (home page). The name of the exhibition is "Savorix" which is going to be Held in south korea. The concept is "Fine Food" in major, qui means clustering Would not we accept Any canned food, fast food, chips, thesis kind of foods. We do not open to the public like Some Other Food exhibitions do, Then only trade visitors. The EXHIBITORS will come from all the World. The categories we Would like to make is in attachment below. We will update the text When the category's share will be done. We need a color can qui correspond well to the "Find Food ', color of our logo qui est in attachment Would be good. You can offer us some photos, images, like photos of fine food corners in supermarkets, gourmet shops like photos of etc. ... You can find links Some of "same" exhibitions in below, qui can give you a guideline of the kind of website we expect. http://en.plumbarrow-fairhall.com/ http://velmontrade.com/ http: //www.tarnicplaza. co.kr We will ask to the winning designer to Develop the full website under Wordpress.
Updates

Project Deadline Extended
Reason: Because we need some modifications to requests.

Target Market(s)

Fine food, gourmet food, "grocery", pastry, bakery

Number of Pages Required

5+ page

Font styles to use
Sans Serif

Colors
886aae
6b449b
e34197
e667a6
9bcb3c
f58947
f37122
ec1f27

Requirements
Must have
• Warm colors, and layout showing the high level of foods, fine foods, gourmet foods
Nice to have
• It would be nice to include the sentence "The new meeting place for the gourmet food in Asia"

```html
<!DOCTYPE html>
<html lang="en">
<head>
<meta charset="utf-8">
<title>Savorix – The Fine Food Event in Asia</title>
<link rel="stylesheet" href="https://fonts.googleapis.com/css2?family=Mulish:wght@300;400;600;700;800&display=swap">
<style>
:root{
  --purple:#6a1a6c;
  --purple-dark:#560f58;
  --magenta:#c8135f;
  --band:#d1105c;
  --ink:#333;
  --muted:#777;
  --rule:#e4e4e4;
  --footer:#262626;
  --footer-bottom:#1c1c1c;
  --footer-text:#cfcfcf;
  --white:#fff;
}
*{box-sizing:border-box;margin:0;padding:0}
html,body{width:1200px;height:2808px;overflow:hidden}
body{font-family:"Mulish",sans-serif;color:var(--ink);background:var(--white);position:relative}
a{color:inherit;text-decoration:none}

/* header */
.site-header{position:absolute;top:0;left:0;width:1200px;height:127px;background:var(--white)}
.brand{position:absolute;left:99px;top:34px}
.brand-name{font-size:42px;font-weight:800;color:var(--purple);letter-spacing:1px;line-height:1}
.brand-tagline{font-size:17px;font-weight:700;color:var(--magenta);margin-top:6px}
.utility-nav{position:absolute;right:96px;top:31px;font-size:12px;color:#555}
.utility-nav span{margin:0 8px;color:#aaa}
.main-nav{position:absolute;left:444px;top:82px;display:flex}
.main-nav a{width:132px;height:45px;display:flex;align-items:center;justify-content:center;font-size:14px;color:#444;
  background:linear-gradient(#fff,#f2f2f2);border:1px solid #e2e2e2;border-bottom:none;margin-right:-1px;
  clip-path:polygon(14px 0,100% 0,100% 100%,0 100%)}

/* hero */
.hero{position:absolute;top:127px;left:0;width:1200px;height:618px;
  background:linear-gradient(120deg,#4b3a3f 0%,#8f7f86 35%,#b8a7a6 55%,#7e6a5a 75%,#a06845 100%)}
.hero::after{content:"";position:absolute;inset:0;background:rgba(90,60,90,.35)}
.hero-content{position:absolute;inset:0;z-index:1;color:var(--white)}
.hero-title{position:absolute;top:178px;width:100%;text-align:center;font-size:60px;font-weight:700;line-height:66px}
.hero-facts{position:absolute;top:360px;left:172px;display:flex}
.fact{display:flex;align-items:flex-start;margin-right:60px}
.fact-icon{width:50px;height:50px;border:2px solid rgba(255,255,255,.8);border-radius:50%;display:flex;align-items:center;justify-content:center;margin-right:14px}
.fact-label{font-size:20px;font-weight:700;letter-spacing:.5px;margin-top:2px}
.fact-value{font-size:11px;line-height:15px;text-transform:uppercase;opacity:.9}
.hero-arrow{position:absolute;top:266px;width:44px;height:44px;border-radius:50%;background:rgba(255,255,255,.18);display:flex;align-items:center;justify-content:center}
.hero-arrow.prev{left:20px}.hero-arrow.next{right:20px}

/* audiences */
.audiences{position:absolute;top:745px;left:0;width:1200px;height:687px}
.audiences .divider{position:absolute;left:600px;top:82px;width:1px;height:520px;background:var(--rule)}
.audience{position:absolute;top:0;width:600px;text-align:center}
.audience.exhibitors{left:0}.audience.visitors{left:600px}
.audience-title{position:absolute;top:86px;width:100%;font-size:42px;font-weight:300;color:#333}
.audience-icon{position:absolute;top:160px;left:214px;width:172px;height:172px;border-radius:50%;background:#f7f7f7;border:1px solid #ececec;display:flex;align-items:center;justify-content:center}
.audience-headline{position:absolute;top:340px;width:100%;font-size:42px;line-height:50px;font-weight:400;color:var(--purple);text-transform:uppercase}
.audience-text{position:absolute;top:454px;left:110px;width:380px;font-size:13px;line-height:27px;color:var(--muted)}
.audience-actions{position:absolute;top:547px;left:140px;display:flex;gap:20px}
.btn{width:159px;height:44px;display:flex;align-items:center;justify-content:center;font-size:14px;text-transform:uppercase;border:1px solid var(--purple)}
.btn-outline{color:var(--purple);background:var(--white)}
.btn-solid{color:var(--white);background:var(--purple)}

/* feature video */
.feature{position:absolute;top:1432px;left:0;width:1200px;height:515px;
  background:linear-gradient(100deg,#6b3a2a 0%,#8a4a3a 25%,#a67a6a 50%,#7a2a3a 72%,#a05a6a 100%)}
.feature::after{content:"";position:absolute;inset:0;background:rgba(150,70,120,.35)}
.feature-content{position:absolute;inset:0;z-index:1;color:var(--white);text-align:center}
.feature-title{position:absolute;top:125px;width:100%;font-size:76px;font-weight:700}
.feature-text{position:absolute;top:218px;left:140px;width:920px;font-size:17px;line-height:28px}
.play{position:absolute;top:283px;left:546px;width:108px;height:108px}

/* access */
.access-band{position:absolute;top:1947px;left:0;width:1200px;height:118px;background:var(--band);color:var(--white);font-size:24px;display:flex;align-items:center;justify-content:center}
.map{position:absolute;top:2065px;left:0;width:1200px;height:397px;background:linear-gradient(135deg,#ecebe7,#e0ded9)}

/* footer */
.site-footer{position:absolute;top:2462px;left:0;width:1200px;height:284px;background:var(--footer);color:var(--footer-text)}
.footer-col{position:absolute;top:45px}
.footer-col h4{font-size:15px;font-weight:400;color:var(--white);text-transform:uppercase;margin-bottom:13px}
.footer-col li{list-style:none;font-size:11.5px;line-height:27px}
.footer-col.links{border-left:1px solid #3a3a3a;padding-left:0;height:205px}
.col-news{left:99px;width:240px}
.col-news p{font-size:11px;line-height:17px}
.email-field{margin-top:12px;width:243px;height:38px;background:var(--white);color:#aaa;font-size:11px;padding:12px 14px}
.subscribe{margin-top:20px;width:97px;height:39px;background:var(--purple);color:var(--white);font-size:13px;display:flex;align-items:center;justify-content:center;text-transform:uppercase}
.col-exhibitors{left:432px}.col-visitors{left:644px}.col-why{left:844px}.col-contact{left:957px;width:150px}
.col-contact li{line-height:22px}
.contact-line{display:flex;align-items:center;gap:8px;margin-top:8px;font-size:11.5px}
.footer-divider{position:absolute;top:45px;width:1px;height:205px;background:#3a3a3a}
.footer-bottom{position:absolute;top:2746px;left:0;width:1200px;height:62px;background:var(--footer-bottom);color:var(--footer-text);font-size:11.5px}
.footer-bottom .copy{position:absolute;left:105px;top:24px}
.social{position:absolute;right:60px;top:22px;display:flex;align-items:center;gap:14px}
.social i{width:14px;height:14px;border-radius:50%;background:#8a8a8a;display:block}
.social .code{margin-left:14px;color:#999}
</style>
</head>
<body>

<header class="site-header">
  <div class="brand">
    <div class="brand-name">SAVORIX</div>
    <div class="brand-tagline">The Fine Food Event in Asia</div>
  </div>
  <nav class="utility-nav"><a>Home</a><span>|</span><a>Asia</a><span>|</span><a>Sitemap</a><span>|</span><a>Contact us</a></nav>
  <nav class="main-nav">
    <a>The Exhibition</a><a>Exhibitors</a><a>Visitors</a><a>Events</a><a>Media</a>
  </nav>
</header>

<section class="hero" role="img" aria-label="Photo of a plated gourmet salad with a wine glass on a restaurant table">
  <div class="hero-content">
    <h1 class="hero-title">The New Meeting Place for the<br>Gourmet Food in Asia</h1>
    <div class="hero-facts">
      <div class="fact">
        <div class="fact-icon"><svg width="24" height="24" viewBox="0 0 24 24" fill="none" stroke="#fff" stroke-width="1.6"><rect x="3" y="5" width="18" height="16" rx="2"/><path d="M3 10h18M8 3v4M16 3v4"/></svg></div>
        <div><div class="fact-label">DATE</div><div class="fact-value">02-03 November, 2017</div></div>
      </div>
      <div class="fact">
        <div class="fact-icon"><svg width="22" height="24" viewBox="0 0 22 24" fill="none" stroke="#fff" stroke-width="1.6"><path d="M11 22s-7-7-7-12a7 7 0 0 1 14 0c0 5-7 12-7 12z"/><circle cx="11" cy="10" r="2.5"/></svg></div>
        <div><div class="fact-label">VENUE</div><div class="fact-value">Hallvern Hall 8B</div></div>
      </div>
      <div class="fact">
        <div class="fact-icon"><svg width="24" height="24" viewBox="0 0 24 24" fill="none" stroke="#fff" stroke-width="1.6"><circle cx="12" cy="12" r="9"/><path d="M12 7v5l3 2"/></svg></div>
        <div><div class="fact-label">OPENING TIMES</div><div class="fact-value">10:00 – 18:00 for the first day<br>10:00 – 17:00 for the second day</div></div>
      </div>
    </div>
    <a class="hero-arrow prev"><svg width="14" height="22" viewBox="0 0 14 22"><path d="M11 2L3 11l8 9" fill="none" stroke="#fff" stroke-width="2"/></svg></a>
    <a class="hero-arrow next"><svg width="14" height="22" viewBox="0 0 14 22"><path d="M3 2l8 9-8 9" fill="none" stroke="#fff" stroke-width="2"/></svg></a>
  </div>
</section>

<section class="audiences">
  <div class="divider"></div>
  <article class="audience exhibitors">
    <h2 class="audience-title">Exhibitors</h2>
    <div class="audience-icon"><svg width="80" height="80" viewBox="0 0 80 80" fill="var(--purple)"><rect x="14" y="12" width="52" height="36" rx="2"/><rect x="19" y="17" width="42" height="26" fill="#f7f7f7"/><path d="M38 48h4v10l12 14-3 2-11-12-11 12-3-2 12-14z"/><path d="M26 38l10-9 7 6 11-12" fill="none" stroke="var(--purple)" stroke-width="3"/></svg></div>
    <p class="audience-headline">40,000 Buyers<br>over 4 days</p>
    <p class="audience-text">Sed ut perspiciatis unde omnis iste natus error sit voluptatem accusantium doloremque laudantium</p>
    <div class="audience-actions"><a class="btn btn-outline">Learn more</a><a class="btn btn-solid">Register now</a></div>
  </article>
  <article class="audience visitors">
    <h2 class="audience-title">Visitors</h2>
    <div class="audience-icon"><svg width="84" height="60" viewBox="0 0 84 60" fill="var(--purple)"><path d="M4 10h76v12a8 8 0 0 0 0 16v12H4V38a8 8 0 0 0 0-16z"/><path d="M58 14v32" stroke="#f7f7f7" stroke-width="2" stroke-dasharray="4 3"/><rect x="14" y="22" width="34" height="4" fill="#f7f7f7"/><rect x="14" y="32" width="24" height="4" fill="#f7f7f7"/></svg></div>
    <p class="audience-headline">Free<br>Admission!</p>
    <p class="audience-text">Sed ut perspiciatis unde omnis iste natus error sit voluptatem accusantium doloremque laudantium</p>
    <div class="audience-actions"><a class="btn btn-outline">Learn more</a><a class="btn btn-solid">Register now</a></div>
  </article>
</section>

<section class="feature" role="img" aria-label="Photo of grilled meats, roasted vegetables and a glass of red wine">
  <div class="feature-content">
    <h2 class="feature-title">Food Exhibition</h2>
    <p class="feature-text">At vero eos et accusamus et iusto odio dignissimos ducimus qui blanditiis praesentium voluptatum deleniti atque corrupti quos dolores et quas molestias excepturi sint occaecati cupiditate non provident</p>
    <svg class="play" viewBox="0 0 108 108"><circle cx="54" cy="54" r="49" fill="none" stroke="#fff" stroke-width="7"/><path d="M42 32l34 22-34 22z" fill="#fff"/></svg>
  </div>
</section>

<div class="access-band">Access to the Show HALLVERN, Sorin-dong Hanbit-gu, Miryeon-si, Gyeongdo, Korea</div>
<div class="map" role="img" aria-label="Street map showing the location of the exhibition venue"></div>

<footer class="site-footer">
  <div class="footer-col col-news">
    <h4>Join our newsletter</h4>
    <p>Alternatively, please fill out the form below to contact me via email.</p>
    <div class="email-field">Enter Your Email</div>
    <a class="subscribe">Subscribe</a>
  </div>
  <div class="footer-divider" style="left:410px"></div>
  <div class="footer-col col-exhibitors">
    <h4>For Exhibitors</h4>
    <ul><li>Exhibitor Registration</li><li>Exhibitor Profile</li><li>Booth Options</li><li>Promote Your Booth</li><li>Official Subcontractors</li><li>Forms &amp; Manuals</li><li>National Pavilion Package</li></ul>
  </div>
  <div class="footer-divider" style="left:622px"></div>
  <div class="footer-col col-visitors">
    <h4>For Visitors</h4>
    <ul><li>Visitors Profile</li><li>Visitor Registration</li><li>Visiting The Show</li><li>Delegation Program</li><li>Business Matching Program</li></ul>
  </div>
  <div class="footer-divider" style="left:822px"></div>
  <div class="footer-col col-why">
    <h4>Why us</h4>
    <ul><li>Customers</li><li>Team</li><li>FAQ</li><li>News</li><li>Others</li></ul>
  </div>
  <div class="footer-divider" style="left:935px"></div>
  <div class="footer-col col-contact">
    <h4>Contact info</h4>
    <ul><li>SAVORIX</li><li>HALLVERN, Sorin-dong Hanbit-gu, Miryeon-si, Gyeongdo, Korea</li></ul>
    <div class="contact-line"><svg width="12" height="12" viewBox="0 0 24 24" fill="#fff"><path d="M6 2l4 4-2 3a13 13 0 0 0 7 7l3-2 4 4-3 4C10 22 2 14 2 5z"/></svg>01234 567 890</div>
    <div class="contact-line"><svg width="12" height="10" viewBox="0 0 24 18" fill="#fff"><path d="M0 0h24v18H0z"/><path d="M0 0l12 9 12-9" fill="none" stroke="#262626" stroke-width="2"/></svg>Contact@domain.com</div>
  </div>
</footer>

<div class="footer-bottom">
  <div class="copy">© 2016. SAVORIX. All rights reserved</div>
  <div class="social">Connect with our social network :<i></i><i></i><i></i><i></i><i></i><span class="code">C16</span></div>
</div>

</body>
</html>
```